Letterhead to Prospective Clients

Create a letterhead (word & canva) that I will use to send letters to prospective clients and also include the Coralwood Estate Partners Logo, My Contact Details and Interchangeable "Suburb". Use the same font and colour pallete

Maris Dulworth | "Suburb" Specialist - Kestrel Bay & Surrounds
Mobile: 0417 862 095
Email: MD@CoralwoodEstatePartners.com.au

```html
<!DOCTYPE html>
<html lang="en">
<head>
<meta charset="utf-8">
<title>Coralwood Estate Partners Letterhead</title>
<link href="https://fonts.googleapis.com/css2?family=Lato:wght@300;400;700&family=Montserrat:wght@400&family=Parisienne&display=swap" rel="stylesheet">
<style>
  :root {
    --navy: #0b1a33;
    --tan: #d4ab7c;
    --ink: #3a3a3a;
    --paper: #ffffff;
    --backdrop: #e4e4e4;
  }
  * { margin: 0; padding: 0; box-sizing: border-box; }
  html, body {
    width: 1153px; height: 1200px; overflow: hidden;
    background: var(--backdrop);
  }
  .letterhead {
    position: absolute; left: 156px; top: 12px;
    width: 840px; height: 1176px;
    background: var(--paper);
    font-family: 'Lato', sans-serif;
    color: var(--ink);
  }
  .brand-name {
    position: absolute; left: 63px; top: 50px;
    color: var(--navy); font-weight: 300;
    text-transform: uppercase; line-height: 1;
  }
  .brand-name .primary { display: block; font-size: 50px; letter-spacing: 5px; }
  .brand-name .secondary { display: block; font-size: 12px; letter-spacing: 6px; margin-top: 25px; padding-left: 58px; }
  .contact {
    position: absolute; left: 513px; top: 69px;
    font-family: 'Montserrat', sans-serif; font-size: 13.5px; color: var(--navy);
    list-style: none;
  }
  .contact li { display: flex; align-items: center; height: 19.5px; }
  .contact svg { width: 13px; height: 11px; margin-right: 12px; fill: var(--navy); }
  .letter-body {
    position: absolute; left: 65px; top: 288px; width: 711px;
    font-size: 15.8px; line-height: 18px;
  }
  .date { margin-bottom: 21px; font-size: 16px; }
  .recipient { font-size: 15.5px; line-height: 19px; margin-bottom: 19px; }
  .salutation { font-size: 20px; font-weight: 700; margin: 20px 0 18px; }
  .paragraph { text-align: justify; margin-bottom: 18px; }
  .closing { margin-top: 38px; }
  .signature {
    font-family: 'Parisienne', cursive; font-size: 38px; line-height: 1; color: #2a2a2a;
    margin-top: 26px; margin-left: 4px;
  }
  .footer-bands { position: absolute; left: 0; bottom: 0; width: 840px; height: 55px; }
  .footer-line {
    position: absolute; right: 18px; bottom: 19px;
    font-family: 'Montserrat', sans-serif; font-size: 10.6px; line-height: 1; color: #ffffff;
    white-space: nowrap;
  }
</style>
</head>
<body>
  <main class="letterhead">
    <header>
      <div class="brand-name">
        <span class="primary">Coralwood</span>
        <span class="secondary">Estate Partners</span>
      </div>
      <ul class="contact">
        <li>
          <svg viewBox="0 0 13 11" aria-hidden="true"><path d="M1 3.5C1 1.5 4 1 6.5 1S12 1.5 12 3.5L10 4.2 9 3H4L3 4.2ZM3.5 5h6l1.5 5H2Z"/></svg>
          0417 862 095
        </li>
        <li>
          <svg viewBox="0 0 13 11" aria-hidden="true"><path d="M0.5 1.5h12v8h-12Z M0.5 1.5 6.5 6l6-4.5" stroke="#fff" stroke-width="0.9"/></svg>
          MD@CoralwoodEstatePartners.com.au
        </li>
      </ul>
    </header>

    <section class="letter-body">
      <p class="date">Feb-03-2022</p>
      <p class="recipient">Mr, Peter Lane<br>President</p>
      <p class="recipient">Northgate Holdings<br>123 Street Name, Suite# 10<br>City, State, 120023</p>
      <p class="salutation">Dear Mr, Peter</p>
      <p class="paragraph">Lorem ipsum dolor sit amet, consectetur adipisicing elit, sed do eiusmod tempor incididunt ut labore et dolore magna aliqua. Ut enim ad minim veniam, quis nostrud exercitation ullamco laboris nisi ut aliquip ex ea commodo consequat. Duis aute irure dolor in reprehenderit in voluptate velit esse cillum dolore eu fugiat nulla pariatur.</p>
      <p class="paragraph">Lorem ipsum dolor sit amet, consectetur adipisicing elit, sed do eiusmod tempor incididunt ut labore et dolore magna aliqua. Ut enim ad minim veniam, quis nostrud exercitation ullamco laboris nisi ut aliquip ex ea commodo consequat. Duis aute irure dolor in reprehenderit in voluptate velit esse cillum dolore eu fugiat nulla pariatur.</p>
      <p class="paragraph">Lorem ipsum dolor sit amet, consectetur adipisicing elit, sed do eiusmod tempor incididunt ut labore et dolore magna aliqua. Ut enim ad minim veniam, quis nostrud exercitation ullamco laboris nisi ut aliquip ex ea commodo consequat.</p>
      <p class="paragraph">Excepteur sint occaecat cupidatat non proident, sunt in culpa qui officia deserunt mollit anim id est laborum. re et dolore magnam aliquam quaerat voluptatem.</p>
      <p class="closing">Regards</p>
      <p class="signature">Evan Harlow</p>
    </section>

    <footer>
      <svg class="footer-bands" viewBox="0 0 840 55" aria-hidden="true">
        <polygon points="0,11 487,11 479,19 0,19" fill="var(--navy)"/>
        <polygon points="0,28 459,28 434,55 0,55" fill="var(--tan)"/>
        <polygon points="498,0 840,0 840,55 447,55" fill="var(--navy)"/>
      </svg>
      <p class="footer-line">Maris Dulworth | "Suburb" Specialist - Kestrel Bay &amp; Surrounds</p>
    </footer>
  </main>
</body>
</html>
```